Build Your Own Shake Menu Design

Menu Design
- will be printed on countertop acrylic menu stands that are a foot by a foot

Files:
- document attached for the menu contents
*file name: SHAKEMENU
- sample menu images (these are giant acrylic menu boards that are in my shop)
*file name: newest shave ice menu, newest spi rolls menu (JPG)
-picture of the shop where the menus will be placed
*file name: shop (PNG)

```html
<!DOCTYPE html>
<html lang="en">
<head>
<meta charset="utf-8">
<title>Shake Menu</title>
<link rel="stylesheet" href="https://fonts.googleapis.com/css2?family=Fira+Sans:wght@600;700;800&family=Fira+Sans+Condensed:wght@600&family=Oleo+Script:wght@400;700&family=Ubuntu:wght@700&family=Yanone+Kaffeesatz:wght@400;500&display=swap">
<style>
:root{
  --red:#c8102e;
  --red-deep:#8a0c1e;
  --ink:#1a1a1a;
  --white:#ffffff;
  --navy:#1c2340;
  --page:#ffffff;
}
*{margin:0;padding:0;box-sizing:border-box}
html,body{width:1040px;height:1200px;overflow:hidden;background:var(--page)}
body{position:relative;font-family:"Fira Sans",sans-serif;color:var(--white)}

/* ---------- shake board ---------- */
.shake-board{position:absolute;left:114px;top:86px;width:812px;height:520px;background:var(--white);box-shadow:0 2px 6px rgba(0,0,0,.25);overflow:hidden}
.shake-board__bg{position:absolute;inset:0}
.board-title{position:absolute;left:0;top:17px;width:280px;height:42px;background:linear-gradient(90deg,var(--ink) 0%,var(--red-deep) 12%,var(--red-deep) 70%,var(--ink) 100%);display:flex;align-items:center;padding-left:34px}
.board-title h1{font-family:"Ubuntu",sans-serif;font-weight:700;font-size:28px;letter-spacing:1.5px;color:var(--white);white-space:nowrap}
.price-box{position:absolute;left:34px;top:73px;width:300px;height:127px;border:1.5px solid var(--white);padding:5px 10px}
.price-row{display:flex;justify-content:space-between;font-weight:700;font-size:16.5px;line-height:27px;white-space:nowrap}
.price-divider{height:1px;background:rgba(255,255,255,.7);margin:4px 8px}
.script-heading{position:absolute;font-family:"Oleo Script",cursive;font-weight:400;font-size:28px;line-height:34px;color:var(--white);letter-spacing:1px;white-space:nowrap}
.base-heading{left:44px;top:208px}
.specialty-heading{left:38px;top:310px}
.option-box{position:absolute;left:34px;width:300px;border:1.5px solid var(--white)}
.option-box--base{top:251px;height:44px;display:flex;justify-content:center;align-items:center;gap:6px}
.option-box--specialty{top:361px;height:77px;display:grid;grid-template-columns:1fr 1fr;justify-items:center;align-content:center;row-gap:9px;padding:0 6px}
.pill{background:var(--white);color:var(--navy);font-family:"Ubuntu",sans-serif;font-weight:700;border-radius:20px;text-align:center;white-space:nowrap}
.option-box--base .pill{font-size:11.5px;letter-spacing:.8px;padding:3px 7px}
.option-box--specialty .pill{font-size:15px;letter-spacing:1px;line-height:20px;padding:1px 10px}
.price-burst{position:absolute;left:245px;top:303px;width:105px;height:46px}
.board-note{position:absolute;left:0;top:452px;width:370px;text-align:center;font-family:"Oleo Script",cursive;font-size:20px;line-height:26px;letter-spacing:.8px}
.additions-title{position:absolute;left:382px;top:42px;width:424px;text-align:center;font-family:"Yanone Kaffeesatz",sans-serif;font-weight:500;font-size:39px;line-height:48px;white-space:nowrap;color:var(--white);transform:rotate(-2deg)}
.additions-tag{position:absolute;left:503px;top:116px;background:var(--white);color:var(--ink);font-family:"Yanone Kaffeesatz",sans-serif;font-size:21px;line-height:26px;padding:2px 8px;white-space:nowrap;transform:rotate(-2deg)}
.additions-list{position:absolute;left:412px;top:169px;width:388px;text-align:center;font-family:"Fira Sans Condensed",sans-serif;font-weight:600;font-size:15px;line-height:28.6px;white-space:nowrap}
.brand-name{position:absolute;left:467px;top:450px;width:300px;text-align:center;font-family:"Fira Sans",sans-serif;font-weight:800;font-size:38px;line-height:48px;color:var(--red)}

/* ---------- drinks ---------- */
.drinks-panel{position:absolute;left:136px;top:680px;width:336px;height:448px;background:linear-gradient(160deg,var(--red) 0%,var(--red) 55%,var(--red-deep) 85%,#4a0a12 100%)}
.drinks-panel h2{position:absolute;top:14px;width:100%;text-align:center;font-family:"Ubuntu",sans-serif;font-weight:700;font-size:28px;letter-spacing:2.5px}
.drink-row{position:absolute;left:27px;width:251px;height:76px}
.drink-row + .drink-row{border-top:1px solid rgba(255,255,255,.8)}
.drink-name{position:absolute;left:-6px;width:120px;top:50%;transform:translateY(-50%);text-align:center;font-weight:800;font-size:13px;letter-spacing:1px;line-height:16px;white-space:nowrap}
.drink-photo{position:absolute;left:110px;top:7px;width:62px;height:62px;border-radius:50%;background:radial-gradient(circle,#e9e9e9 0%,#ffffff 70%)}
.drink-price{position:absolute;left:203px;top:50%;transform:translateY(-50%);font-weight:800;font-size:14px;letter-spacing:1px}

/* ---------- spoons ---------- */
.spoons-panel{position:absolute;left:507px;top:731px;width:439px;height:314px;background:linear-gradient(150deg,var(--red) 0%,var(--red) 45%,var(--red-deep) 75%,#2a0a0e 100%)}
.spoons-panel h2{position:absolute;top:20px;width:100%;text-align:center;font-family:"Ubuntu",sans-serif;font-weight:700;font-size:23px;letter-spacing:2px;white-space:nowrap}
.spoons-price{position:absolute;left:78px;top:65px;width:287px;height:35px;background:var(--white);border-radius:18px;color:var(--red);display:flex;align-items:center;justify-content:center;gap:8px;white-space:nowrap}
.spoons-price strong{font-size:24px;font-weight:800}
.spoons-price span{font-size:16px;font-weight:600;letter-spacing:1.5px}
.color-list{position:absolute;left:24px;top:134px;list-style:none}
.color-list li{font-weight:800;font-size:15px;letter-spacing:1.8px;height:56px;display:flex;align-items:flex-start;white-space:nowrap}
.color-list li::before{content:"";width:6px;height:6px;border-radius:50%;background:var(--white);margin:6px 10px 0 0}
.spoons-photo{position:absolute;left:195px;top:40px;width:238px;height:250px;border-radius:30px;background:radial-gradient(ellipse at 60% 50%,rgba(214,120,200,.55) 0%,rgba(120,170,230,.35) 40%,rgba(200,16,46,0) 75%)}
</style>
</head>
<body>

<section class="shake-board">
  <svg class="shake-board__bg" width="812" height="520" viewBox="0 0 812 520" aria-hidden="true">
    <defs>
      <linearGradient id="leftFade" x1="0" y1="0" x2="0" y2="1">
        <stop offset="0" stop-color="#c8102e"/>
        <stop offset=".84" stop-color="#c8102e"/>
        <stop offset=".93" stop-color="#5a0b15"/>
        <stop offset="1" stop-color="#1a1a1a"/>
      </linearGradient>
      <linearGradient id="bannerFade" x1="0" y1="0" x2="1" y2="0">
        <stop offset="0" stop-color="#1a1a1a"/>
        <stop offset=".6" stop-color="#1a1a1a"/>
        <stop offset="1" stop-color="#8a0c1e"/>
      </linearGradient>
    </defs>
    <polygon points="0,0 812,0 812,8 404,10 412,200 412,520 0,520" fill="url(#leftFade)"/>
    <rect x="412" y="114" width="388" height="331" fill="#c8102e"/>
    <polygon points="362,28 812,18 812,105 390,130" fill="url(#bannerFade)"/>
    <polygon points="362,28 390,130 380,131" fill="#ffffff"/>
  </svg>

  <div class="board-title"><h1>SHAKE MENU</h1></div>

  <div class="price-box">
    <p class="price-row"><span>15 ounce Regular</span><span>$5.75</span></p>
    <p class="price-row"><span>15 ounce specialty Base</span><span>$6.25</span></p>
    <div class="price-divider"></div>
    <p class="price-row"><span>18 ounce Large</span><span>$5.99</span></p>
    <p class="price-row"><span>18 ounce Specialty Base</span><span>$6.49</span></p>
  </div>

  <h2 class="script-heading base-heading">Choose Your Base</h2>
  <div class="option-box option-box--base">
    <span class="pill">STANDARD BASE</span>
    <span class="pill">VAN</span>
    <span class="pill">CHOCOLATE</span>
  </div>

  <h2 class="script-heading specialty-heading">Specialty Bases</h2>
  <svg class="price-burst" viewBox="0 0 110 56" preserveAspectRatio="none" aria-label="$0.50">
    <polygon fill="#ffffff" points="55,0 62,10 74,3 76,14 92,9 88,20 108,20 96,28 110,36 92,38 98,50 80,45 76,56 64,47 55,56 46,47 34,56 30,45 12,50 18,38 0,36 14,28 2,20 22,20 18,9 34,14 36,3 48,10"/>
    <text x="55" y="34" text-anchor="middle" font-family="Fira Sans, sans-serif" font-weight="700" font-size="17" fill="#1a1a1a">$0.50</text>
  </svg>
  <div class="option-box option-box--specialty">
    <span class="pill">MINT</span>
    <span class="pill">STRAWBERRY</span>
    <span class="pill">ESPRESSO</span>
    <span class="pill">CHEESECAKE</span>
  </div>

  <p class="board-note">that it comes with free whip<br>cream and a cherry</p>

  <h2 class="additions-title">Choose Up To 2 Items For Your Shake</h2>
  <p class="additions-tag">*list of additions to choose from *</p>

  <p class="additions-list">
    Cookie Dough - Peanut Butter Cup - Crispy Bar<br>
    Mint Thins - Toffee - Choco Chip - Graham Crackers<br>
    Cocoa Cookie - Chocolate Chips - White Chocolate Chips<br>
    Rainbow Sprinkles - Cupcake Bites - Candy Gems Nuts<br>
    Almonds - Strawberries - Cherries Captain Crisp<br>
    Banana - Cinnamon Crisp Fruity Flakes<br>
    Cocoa Flakes Peanut Butter Drizzle<br>
    Chocolate Drizzle - Strawberry Drizzle<br>
    Raspberry Drizzle - Marshmallow Drizzle
  </p>

  <p class="brand-name">Swirl Lab</p>
</section>

<section class="drinks-panel">
  <h2>DRINKS</h2>
  <div class="drink-row" style="top:53px"><p class="drink-name">WATER</p><div class="drink-photo" role="img" aria-label="Photo of a bottle of water"></div><p class="drink-price">$1.00</p></div>
  <div class="drink-row" style="top:129px"><p class="drink-name">COLA</p><div class="drink-photo" role="img" aria-label="Photo of a bottle of cola"></div><p class="drink-price">$1.99</p></div>
  <div class="drink-row" style="top:206px"><p class="drink-name">LEMON SODA</p><div class="drink-photo" role="img" aria-label="Photo of a bottle of lemon soda"></div><p class="drink-price">$1.99</p></div>
  <div class="drink-row" style="top:282px"><p class="drink-name">TEA</p><div class="drink-photo" role="img" aria-label="Photo of a cup of tea"></div><p class="drink-price">$1.99</p></div>
  <div class="drink-row" style="top:358px"><p class="drink-name">SPORT DRINK<br>FRUIT PUNCH</p><div class="drink-photo" role="img" aria-label="Photo of a bottle of fruit punch sport drink"></div><p class="drink-price">$1.99</p></div>
</section>

<section class="spoons-panel">
  <div class="spoons-photo" role="img" aria-label="Photo of four colour changing plastic spoons"></div>
  <h2>COLOR CHANGING SPOONS</h2>
  <p class="spoons-price"><strong>$0.50</strong><span>COME IN 3 COLORS</span></p>
  <ul class="color-list">
    <li>WHITE TO BLUE</li>
    <li>PINK TO PURPLE</li>
    <li>WHITE TO CONFETTI</li>
  </ul>
</section>

</body>
</html>
```